Poster Design for Film: 'Tres Lunas'

Tres Lunas means "two times" in Spanish. This short film is based on the true story of Cuban refugee during the take over of the Ordaz regime in 1959 and how is experiences and stories affected his children and grandchildren. Tres Lunas tells the story of Daniel- a recent grad who is forced to choose between his critically ill grandfather, the business opportunity of a lifetime, and maintaining a relationship with his love interest, Margaret. Through his grandfather's recollections as a young man in 1950's Cuba, Daniel gains a new outlook on life and the things that matter most.

This poster should evoke the drama and truth that the film approaches in a cinematic manner while maintaining the influences of true Cuban culture and history as perceived by a Miami audience today.

For more information please take a look at our fund raising site:
http://www.fundhaven.example/projects/tres-lunas

The grandfather's current life (the Cuban revolutionary/refugee as an old man):
www.clipvault.example/41592867
password: treslunas

A quick teaser of the film, exploring the lives of Daniel (the protagonist; grandson to Cuban refugee/revolutionary) and Meg (Daniel's love interest he neglects to commit to):

http://www.streamtube.example/watch?v=QbRtPwXnLeK

Please let me know if you would like any stills of the film, have any questions, etc. Thanks!

Hey all! So sorry for the delay on the stills- we had some serious technical issues, but now they are up!

Please let me know if you have any questions. We'll be uploaded more stills to choose from tonight.

Thanks!

Hey all!
Unless you need something in specific, I have just uploaded the final stills for the poster. Feel free to use any of the images, but please keep in mind that the main characters are Dan (the grandson), and his grandfather Arturo both young and old. In other words- the three guys.

Please let me know if you have any questions. Thanks! 

Here are some small text details for the bottom of the poster:

A Copper Lantern Production in association with BrightKiln Studios and the Coastal Pines University. Starring Brett Solano, Celina Fuentes, Omar Bustillo, Lucia Ortega, Farid Khoury. Written, Directed, & Produced by Marcos Ibarra. Director of Photography Tomas Varela. Edited by Marcos Ibarra & Tomas Varela.

Hey designers!

I've just uploaded a new still of the main character. Please try to include it in your design, as it is preferred over the other stills of the main character.

Thanks!

I've just uploaded two small logos to be featured on the bottom of the poster.

Thanks!

Target Market(s)

Hollywood. Cuban-Americans. Miamians. Film Critics. Students. Professors.

Adults based in Los Angeles and Miami aged 21-50 that speak English and Spanish and are in the art and entertainment industry.

Industry/Entity Type

Business

Requirements
Must have
• Must evoke the style of Cuba in the late 1950's while staying true to current day culture/style for 20-somethings in America (specifically LA, NYC, Miami).
Nice to have
• A sort of serious, almost stoic style that could possibly evoke a melancholic reaction.
Should not have
• Anything that evokes a daytime soap opera.

```html
<!DOCTYPE html>
<html lang="en">
<head>
<meta charset="utf-8">
<title>Tres Lunas – Film Poster</title>
<link rel="stylesheet" href="https://fonts.googleapis.com/css2?family=Anton&family=Antonio:wght@400;600;700&family=Oswald:wght@400;500&display=swap">
<style>
  :root {
    --paper: #ebe9da;
    --paper-edge: #c9ccb4;
    --ink-green: #2f4a2c;
    --title-light: #e98f2a;
    --title-dark: #c9581a;
    --credit: #c5561d;
    --url: #d8861f;
    --flag-orange: #eba779;
    --flag-blue: #a6d3d4;
    --badge: #3f5fa8;
    --frame: #f4f2e8;
  }
  * { margin: 0; padding: 0; box-sizing: border-box; }
  html, body { width: 813px; height: 1200px; overflow: hidden; background: var(--paper); }
  .poster {
    position: relative; width: 813px; height: 1200px; overflow: hidden;
    background:
      radial-gradient(ellipse at 100% 0%, rgba(60,80,50,.45), transparent 30%),
      radial-gradient(ellipse at 0% 100%, rgba(150,150,120,.25), transparent 40%),
      radial-gradient(ellipse at 50% 40%, #f1efe2, var(--paper) 60%, var(--paper-edge));
    font-family: "Oswald", sans-serif;
  }
  .coins {
    position: absolute; left: 442px; top: 36px; width: 198px; height: 207px;
    border-radius: 50%;
    background: radial-gradient(circle at 45% 40%, #d8d3c2, #a9a594 70%, #8c8878);
    opacity: .85;
  }
  .presenter {
    position: absolute; left: 23px; top: 184px;
    color: var(--ink-green); font-size: 25px; line-height: 31px;
    font-variant: small-caps; font-weight: 500;
  }
  .title { position: absolute; left: 0; top: 250px; width: 813px; height: 140px; }
  .title text { font-family: "Anton", sans-serif; font-size: 172px; }
  .title .first { fill: var(--title-light); }
  .title .second { fill: var(--title-dark); }

  .still { position: absolute; border: 3px solid var(--frame); }
  .still--lead { left: 6px; top: 394px; width: 497px; height: 278px;
    background:
      linear-gradient(90deg, rgba(20,24,26,.55), transparent 45%),
      radial-gradient(ellipse at 35% 40%, #8a7466 0%, #4a4542 28%, transparent 45%),
      linear-gradient(120deg, #23292c, #56636a 50%, #9fabaa 75%, #5e6a6c); }
  .still--elder { left: 509px; top: 397px; width: 295px; height: 87px;
    background: linear-gradient(90deg, #5a4a3c, #8e7a66 45%, #a99482 65%, #c8c2b6); }
  .still--love { left: 509px; top: 490px; width: 295px; height: 90px;
    background: linear-gradient(90deg, #4f5c56, #7c6a5a 50%, #a88472 65%, #3a2a24); }
  .still--couple { left: 509px; top: 586px; width: 295px; height: 86px;
    background: linear-gradient(90deg, #201a18, #9a7462 40%, #5a3e34 65%, #2a201c); }

  .flag { position: absolute; left: 0; top: 690px; width: 813px; height: 270px; }
  .credits {
    position: absolute; left: 0; width: 813px; top: 694px; text-align: center;
    color: var(--credit); font-family: "Antonio", sans-serif; font-weight: 600;
    font-variant: small-caps; font-size: 27px; line-height: 31px; letter-spacing: .5px;
  }
  .credits .edit-line { font-size: 23px; }
  .release { position: absolute; left: 0; top: 835px; width: 813px; height: 120px; }
  .release .release-line { font-family: "Antonio", sans-serif; font-weight: 700; font-size: 62px; fill: var(--credit); }
  .release .release-site { font-family: "Antonio", sans-serif; font-weight: 600; font-size: 27px; fill: var(--url); }
  .partner-url {
    position: absolute; top: 1122px; color: var(--url);
    font-family: "Antonio", sans-serif; font-weight: 600; font-size: 21px;
  }
  .partner-url--production { left: 28px; }
  .partner-url--studio { left: 305px; }
  .badge {
    position: absolute; left: 648px; top: 1052px; width: 128px; height: 128px;
    border-radius: 50%; background: var(--badge); opacity: .8;
  }
</style>
</head>
<body>
<main class="poster">
  <div class="coins" role="img" aria-label="Stack of vintage Cuban coins"></div>

  <p class="presenter">A Copper Lantern Production in association with<br>BrightKiln Studios and the Coastal Pines University.</p>

  <svg class="title" viewBox="0 0 813 140" role="img" aria-label="Tres Lunas">
    <text x="19" y="134" textLength="781" lengthAdjust="spacingAndGlyphs"><tspan class="first">TRES</tspan><tspan class="second">LUNAS</tspan></text>
  </svg>

  <div class="still still--lead" role="img" aria-label="Film still of the grandson in profile by a window"></div>
  <div class="still still--elder" role="img" aria-label="Film still of the grandfather"></div>
  <div class="still still--love" role="img" aria-label="Film still of the love interest"></div>
  <div class="still still--couple" role="img" aria-label="Film still of the couple together"></div>

  <svg class="flag" viewBox="0 0 813 270" aria-hidden="true">
    <rect x="256" y="29" width="557" height="87" fill="var(--flag-blue)" opacity=".75"/>
    <rect x="0" y="120" width="290" height="140" fill="var(--flag-orange)" opacity=".35"/>
    <polygon points="0,8 314,140 0,262" fill="var(--flag-orange)" opacity=".8"/>
    <polygon points="96,24 114,78 171,78 125,111 142,165 96,132 50,165 67,111 21,78 78,78" fill="var(--frame)" opacity=".95"/>
  </svg>

  <p class="credits">
    Starring Brett Solano, Celina Fuentes, Omar Bustillo, Lucia Ortega, Farid Khoury.<br>
    Written, Directed, &amp; Produced by Marcos Ibarra. Director of Photography Tomas Varela.<br>
    <span class="edit-line">Edited by Marcos Ibarra &amp; Tomas Varela</span>
  </p>

  <svg class="release" viewBox="0 0 813 120">
    <text class="release-line" x="177" y="66" textLength="482" lengthAdjust="spacingAndGlyphs">IN THEATERS THIS SUMMER</text>
    <text class="release-site" x="288" y="112" textLength="234" lengthAdjust="spacingAndGlyphs">WWW.TRESLUNASFILM.COM</text>
  </svg>

  <p class="partner-url partner-url--production">WWW.COPPERLANTERN.EXAMPLE</p>
  <p class="partner-url partner-url--studio">WWW.BRIGHTKILN.EXAMPLE</p>
  <div class="badge" role="img" aria-label="Partner badge"></div>
</main>
</body>
</html>
```